Elegant invitation for prestigious fund raising event

Background
The Lanterns of Willow is a very prestigious fund raising event. It is a sit down dinner, gala type evening with a presentation and auction.
There are three of these event being held at venues around western North Carolina. The areas where these are being held all have one thing in common, they are in the Appalachian Mountains and the craft of quilt making. As you will see from the Concept Boards attached why a mountain theme and quilt “design feel” is being used. One very important point - we don’t want this design to look like an actual quilt.

See the concept board on page 4, which we can’t use that is from another artist but is one good interpretation of the idea and one way to stylize the picture with a “quilt” interpretation and feel. We do not want a literal quilt representation but are looking for an artistic way on how best to interpret what the quilt represents - the feel of “stitching together” the different things across our region that make us all unique but yet bind us all as one.

The Brief:
We want to develop an elegant invitation for these events.
We have develop as save the date (attached) and all we want to use of this is the wording “Lanterns of Willow” we do not like the icon above it.
Also attached is the wording for the invitation, along with the new picture we want to use (taken from the inspiration boards)

Size, fold, color and paper:

Around 5x7 inches, but open to any dimension if you have an idea that will work in a totally different size. Ideally try and stick to something that will fit a standard envelope so that we don’t need to make a special envelope

Fold – up to you if it has a fold or not and which way it folds. Our thought is that it will need a fold to keep it up market but open to any suggestions.
We are happy to print this on a textured paper if you have suggestions. It will be professionally digital printed so the paper needs to be suitable for digital printing

Color. The inspiration boards show the color palette. We have started out in the save the dates with the navy with reversed out white but again totally up to you to use anything from that color palette.
Updates

Target Market(s)

Up market, around 50 - 65 years old, many are retired, very wealthy

Industry/Entity Type

Event

Requirements
Must have
• See brief attached
Nice to have
• See brief attached
Should not have
• See brief attached

```html
<!DOCTYPE html>
<html lang="en">
<head>
<meta charset="utf-8">
<title>Lanterns of Willow — Invitation</title>
<link rel="stylesheet" href="https://fonts.googleapis.com/css2?family=Montserrat:wght@200;700;800&family=Quicksand:wght@500;700&display=swap">
<style>
  :root {
    --page: #ffffff;
    --wash-yellow: #f5ea86;
    --wash-peach: #f6cf95;
    --wash-cream: #f3e8a8;
    --scene-gold: #f5b43a;
    --scene-blue: #5a8fd2;
    --scene-green: #3d5622;
    --scene-dark: #1e2716;
    --ink: #1c1a17;
    --title: #fbf6ee;
    --fold: #9a8f80;
  }
  * { margin: 0; padding: 0; box-sizing: border-box; }
  html, body {
    width: 1200px; height: 1000px; overflow: hidden;
    background: var(--page);
  }
  .invitation-spread {
    position: absolute; left: 0; top: 68px;
    width: 1200px; height: 859px;
  }
  .background-wash {
    position: absolute; inset: 0;
    background: linear-gradient(160deg, var(--wash-yellow) 0%, var(--wash-peach) 50%, var(--wash-cream) 100%);
  }
  .fold-vertical {
    position: absolute; left: 599px; top: 0; width: 1px; height: 428px;
    background: rgba(255,255,255,.35);
  }
  .fold-horizontal {
    position: absolute; left: 0; top: 427px; width: 1197px; height: 1px;
    background: var(--fold);
  }
  .cover-scene {
    position: absolute; left: 0; top: 428px; width: 600px; height: 431px;
    background: linear-gradient(180deg,
      var(--scene-gold) 0%, var(--scene-blue) 45%, var(--scene-green) 78%, var(--scene-dark) 100%);
  }
  .cover-title {
    position: absolute; left: 88px; top: 602px;
    color: var(--title);
    font-family: "Montserrat", sans-serif;
    line-height: 1;
  }
  .cover-title__lead {
    display: block; font-weight: 200; font-size: 56px; letter-spacing: 1px;
  }
  .cover-title__main {
    display: block; font-weight: 800; font-size: 112px; letter-spacing: -4px;
    margin-top: 13px; margin-left: -4px;
  }
  .invite-copy, .event-details {
    position: absolute; left: 600px; width: 600px; text-align: center;
    color: var(--ink);
  }
  .invite-copy {
    top: 147px;
    font-family: "Quicksand", sans-serif; font-weight: 500;
    font-size: 16px; line-height: 20px; letter-spacing: .4px;
  }
  .invite-copy p + p { margin-top: 21px; }
  .invite-copy strong { font-weight: 700; }
  .event-details {
    top: 554px; list-style: none;
    font-family: "Montserrat", sans-serif; font-weight: 700;
    font-size: 15px; letter-spacing: .5px; line-height: 22px;
  }
  .event-details li + li { margin-top: 21px; }
  .event-details .event-details__dress { margin-top: 73px; }
  .event-details sup { font-size: 9px; vertical-align: 6px; line-height: 0; }
</style>
</head>
<body>
  <main class="invitation-spread">
    <div class="background-wash" role="img" aria-label="Patchwork mosaic texture in soft yellow, peach and rose tones"></div>
    <div class="fold-vertical"></div>
    <div class="fold-horizontal"></div>

    <div class="cover-scene" role="img" aria-label="Painted photo of a golden sunset over misty blue mountain ridges with forest in the foreground"></div>
    <h1 class="cover-title">
      <span class="cover-title__lead">LANTERNS OF</span>
      <span class="cover-title__main">WILLOW</span>
    </h1>

    <section class="invite-copy">
      <p>You are cordially invited to the</p>
      <p><strong>Second Annual Lanterns of Willow</strong> on the <strong>plateau</strong>.</p>
      <p>Please join us for an elegant and entertaining<br>affair benefiting the healthcare in our region.</p>
    </section>

    <ul class="event-details">
      <li>6<sup>TH</sup> OF JUNE, 2016</li>
      <li>THE MEADOW AT CEDAR HOLLOW LODGE</li>
      <li>BEGINNING AT 5:30PM</li>
      <li>VALET PARKING</li>
      <li class="event-details__dress">COCKTAIL ATTIRE • VALET PARKING</li>
    </ul>
  </main>
</body>
</html>
```